White Paper and One-Page Advertisement for TELVAMORE-QX

I need both documents to be better formatted and designed so they look professional, not something someone with mediocre word skills put together. They will go out to 1000s of industry professionals, and they need to look sharp. I need them to have my company's color palate logo, and branding on it similar to how it is now, but better. Please do not change any of the written content, but it can be arranged in any other format you think is better. Smart art and things i've already used can be omitted in favor of better designs. The developer is free to use their creativity. White paper should not be longer than the three pages unless necessary.

Target Market(s)

Life Sciences supply chain professionals

Colors
33b8a4
0592cd
9bcb3c
fbee3e
3277b5

Requirements
Must have
• Must be professional looking and not look like something done in word. Please use the color palate as seen on the documents.
Should not have
• Any changes to the written content.

```html
<!DOCTYPE html>
<html lang="en">
<head>
<meta charset="utf-8">
<title>TELVAMORE-QX One-Page Advertisement</title>
<link rel="stylesheet" href="https://fonts.googleapis.com/css2?family=Montserrat:wght@400;500;600;700&display=swap">
<style>
:root{
  --blue:#3277b5;
  --blue-bright:#2a7fc8;
  --teal:#1e7f6d;
  --teal-light:#33b8a4;
  --lime:#9bcb3c;
  --lime-soft:#b9e35a;
  --yellow:#fbee3e;
  --ink:#2b2b2b;
  --page:#ffffff;
  --backdrop:#ffffff;
}
*{box-sizing:border-box;margin:0;padding:0}
html,body{width:1200px;height:1200px;overflow:hidden;background:var(--backdrop)}
body{font-family:"Montserrat",Arial,sans-serif;color:var(--ink);position:relative}
.flyer{position:absolute;left:170px;top:43px;width:860px;height:1114px;background:var(--page);overflow:hidden;box-shadow:0 3px 10px rgba(0,0,0,.25)}
.hero-shapes{position:absolute;left:0;top:0}
.brand{position:absolute;left:60px;top:128px;width:260px;display:flex;align-items:center;justify-content:center;gap:10px}
.brand-dot{width:22px;height:22px;border-radius:50%;background:var(--teal)}
.brand-name{font-size:28px;font-weight:700;color:var(--teal);letter-spacing:.5px}
.benefits{position:absolute;left:40px;top:224px;width:300px;color:#fff}
.benefits h2{font-size:28px;font-style:italic;font-weight:700;color:var(--yellow);margin-bottom:10px}
.benefits ul{list-style:none}
.benefits li{position:relative;padding-left:25px;font-size:13.5px;font-weight:600;line-height:17px;margin-bottom:8px}
.benefits li::before{content:"";position:absolute;left:2px;top:4px;width:10px;height:10px;border-radius:50%;background:var(--yellow)}
.benefits li::after{content:"";position:absolute;left:5px;top:6px;width:3px;height:4px;border:solid var(--blue);border-width:0 1.5px 1.5px 0;transform:rotate(40deg)}
.section-head{position:absolute;left:40px;width:777px;height:32px;border-bottom:1.5px solid var(--lime)}
.section-head .tab{position:absolute;left:0;top:0;height:32px;background:var(--teal);color:var(--yellow);font-size:21px;font-weight:700;padding:3px 12px 0 12px;clip-path:polygon(0 0,100% 0,calc(100% - 6px) 100%,0 100%)}
.section-head .slash{position:absolute;top:0;width:10px;height:32px;background:var(--lime);transform:skewX(22deg)}
.points{position:absolute;left:40px;width:760px;list-style:none}
.points li{position:relative;padding-left:25px;font-size:16px;line-height:20px;margin-bottom:6px}
.points li::before{content:"";position:absolute;left:2px;top:5px;width:10px;height:10px;border-radius:50%;background:var(--teal)}
.points li::after{content:"";position:absolute;left:5px;top:7px;width:3px;height:4px;border:solid #fff;border-width:0 1.5px 1.5px 0;transform:rotate(40deg)}
.process{position:absolute;left:78px;top:707px}
.process text{font-family:"Montserrat",Arial,sans-serif;font-size:14.5px;font-weight:600;fill:#fff}
.promise{position:absolute;left:42px;top:1005px;width:770px;font-size:16px;line-height:20px}
.footer{position:absolute;left:0;top:1060px;width:860px;height:54px}
.footer-item{position:absolute;top:1068px;display:flex;align-items:center;gap:12px;font-size:16.5px;font-weight:600}
.footer-item.phone{left:44px;color:#fff}
.footer-item.mail{left:298px;color:var(--ink)}
.footer-item.web{left:564px;color:var(--ink)}
</style>
</head>
<body>
<div class="flyer">
  <svg class="hero-shapes" width="860" height="530" viewBox="0 0 860 530">
    <polygon points="0,208 342,208 323,267 398,530 0,530" fill="var(--blue)"/>
    <g role="img" aria-label="Photo of three smiling people at a traditional ceremony, one adjusting another's sleeve">
      <defs>
        <linearGradient id="photoTone" x1="0" y1="0" x2="1" y2="1">
          <stop offset="0" stop-color="#5a3a2c"/>
          <stop offset=".5" stop-color="#7a5a45"/>
          <stop offset="1" stop-color="#2f5f66"/>
        </linearGradient>
      </defs>
      <polygon points="405,0 860,0 860,530 398,530 323,267" fill="url(#photoTone)"/>
    </g>
    <line x1="405" y1="0" x2="323" y2="267" stroke="var(--blue-bright)" stroke-width="4"/>
  </svg>

  <div class="brand">
    <span class="brand-dot"></span>
    <span class="brand-name">TELVAMORE-QX</span>
  </div>

  <section class="benefits">
    <h2>BENEFITS</h2>
    <ul>
      <li>Reduce write-offs by selling excess and obsolete materials, equipment, spare parts, etc.</li>
      <li>Buy quality materials at a reduced price.</li>
      <li>Market materials if an original supplier</li>
      <li>Donate material to researchers</li>
      <li>Acquire donated materials</li>
      <li>Collaborate and consort to reduce supply chain risk such as mutual aid agreements, joint supplier audits, etc.</li>
    </ul>
  </section>

  <div class="section-head" style="top:548px">
    <div class="tab" style="width:192px">Our Platform</div>
    <div class="slash" style="left:192px"></div>
  </div>
  <ul class="points" style="top:596px">
    <li>A multi-vendor marketplace for the life science community to transact pre-market and after-market materials and equipment</li>
    <li>Researchers, manufactures, &amp; original suppliers can create an account to buy, sell, or donate materials</li>
  </ul>

  <svg class="process" width="680" height="142" viewBox="0 0 680 142">
    <polygon points="0,18 148,18 148,0 218,71 148,140 148,123 0,123" fill="var(--blue-bright)"/>
    <polygon points="170,18 300,18 300,0 370,71 300,140 300,123 170,123 220,71" fill="var(--teal)"/>
    <polygon points="323,18 455,18 455,0 525,71 455,140 455,123 323,123 373,71" fill="var(--blue-bright)"/>
    <polygon points="478,18 608,18 608,0 676,71 608,140 608,123 478,123 528,71" fill="var(--teal)"/>
    <text x="34" y="66">Authentication &amp;</text>
    <text x="34" y="84">terms of quality</text>
    <text x="239" y="75">Set up store</text>
    <text x="367" y="49">Seamlessly</text>
    <text x="390" y="67">trasnact and</text>
    <text x="390" y="85">request for</text>
    <text x="367" y="103">information</text>
    <text x="542" y="66">Check out</text>
    <text x="542" y="84">and sign</text>
  </svg>

  <ul class="points" style="top:874px">
    <li>Part 11 compliant signature and authentication</li>
    <li>Leverages industry auditing skills to facilitate compliant and transparent transactions</li>
    <li>Some of the best and industry vendors and software used</li>
  </ul>

  <div class="section-head" style="top:966px">
    <div class="tab" style="width:180px">Our Promise</div>
    <div class="slash" style="left:180px"></div>
  </div>
  <p class="promise">A greener, more cost-efficient, and quality driven supply chain through a collaborative life sciences marketplace.</p>

  <svg class="footer" width="860" height="54" viewBox="0 0 860 54">
    <rect width="860" height="54" fill="var(--teal)"/>
    <polygon points="232,0 860,0 860,36 252,36" fill="var(--lime-soft)"/>
    <line x1="236" y1="0" x2="256" y2="40" stroke="#fff" stroke-width="3"/>
  </svg>
  <div class="footer-item phone">
    <svg width="22" height="22" viewBox="0 0 24 24"><path d="M6.6 3.5l2.6 3.4-1.6 2.2c1 2.2 3 4.3 5.3 5.4l2.2-1.6 3.4 2.6-1.5 3.2c-6.3 0-13.6-7.3-13.6-13.6z" fill="none" stroke="#fff" stroke-width="1.6" stroke-linejoin="round"/></svg>
    800-555-TLVQ
  </div>
  <div class="footer-item mail">
    <svg width="22" height="16" viewBox="0 0 22 16"><rect x="1" y="1" width="20" height="14" fill="var(--teal)"/><path d="M1 1l10 8 10-8" fill="none" stroke="#fff" stroke-width="1.5"/></svg>
    info@telvamoreqx.com
  </div>
  <div class="footer-item web">
    <svg width="20" height="20" viewBox="0 0 20 20" fill="none" stroke="var(--teal)" stroke-width="1.4"><circle cx="10" cy="10" r="8.5"/><ellipse cx="10" cy="10" rx="4" ry="8.5"/><path d="M1.5 10h17M3 5.5h14M3 14.5h14"/></svg>
    www.telvamoreqx.com
  </div>
</div>
</body>
</html>
```